Upcoming lecture sponsored by a church on an important topic

We have a Reformation The Speech coming up at the end of October on the topic of law and gospel. I thought it might be cool to use a flyer that looks like it was from that day and age. Picture what Conrad Velmer would advertise things on kind of an old church/reformation type format. It will be sponsored by our church, and we have a paragraph or two to describe the lecture that would be included on the flyer. We would also want it formatted so that it could be printed on postcards and mailed to churches and individuals.

The flyer should have the following paragraph...

The distinction between the law and the gospel is the most important distinction in the Christian faith. Conrad Velmer: “Distinguishing between the law and the gospel is the highest art in Christendom, one who every person who values the name Christian ought to recognize, know, and possess.” The distinction between the law and the gospel is of great comfort for the child of God. “For the law was given by Moses, but grace and truth came by Jesus Christ” (John 1:17). For these reasons, the distinction between the law and the gospel is the most heavily assaulted doctrine in the Christian faith. This Reformation Day, join us for an explanation and defense of the great distinction between God’s good law and God’s glorious gospel.

And the flyer should have the following information...

Topic: The Steady Word and the Bright Promise
Date and Time: Tuesday, October 31, 2023 at 7:30pm
Host: Harrow Creek Fellowship Church
Speaker: Rev. Gerald Voskuil
Venue: The Marlow Hall, 5172 Brenton Avenue, Hudsonville, MI 49318
Format: Lecture followed by Q&A and refreshments

00AB8E
00BBA5
67D7C9
C6EFE9
E9F9F6

• The color scheme that I would like to have is a teal color (the same color as found at www.brackenhollowchapel.com

```html
<!DOCTYPE html>
<html lang="en">
<head>
<meta charset="utf-8">
<title>Law and Gospel – Reformation Day Lecture</title>
<link rel="stylesheet" href="https://fonts.googleapis.com/css2?family=Playfair+Display:wght@400&family=Poppins:wght@300;500&display=swap">
<style>
  :root {
    --backdrop: #808080;
    --paper: #ffffff;
    --ink: #1e1e1e;
    --title: #ffffff;
    --teal-deep: #00AB8E;
    --teal: #00BBA5;
    --teal-soft: #67D7C9;
    --teal-pale: #C6EFE9;
    --teal-mist: #E9F9F6;
    --teal-shadow: #0c4a42;
    --teal-night: #073430;
  }
  * { box-sizing: border-box; margin: 0; padding: 0; }
  html, body { width: 1199px; height: 1200px; overflow: hidden; }
  body { background: var(--backdrop); position: relative; }

  .flyer {
    position: absolute;
    left: 195px; top: 76px;
    width: 810px; height: 1047px;
    background: var(--paper);
    overflow: hidden;
  }

  .hero {
    position: absolute; left: 0; top: 0;
    width: 810px; height: 563px;
    background:
      radial-gradient(ellipse 150px 210px at 700px 180px, rgba(233,249,246,.8), transparent 70%),
      linear-gradient(90deg, var(--teal-pale) 0%, var(--teal-soft) 30%, var(--teal-deep) 55%, var(--teal-shadow) 78%, var(--teal-night) 100%);
  }
  .hero-figure {
    position: absolute; left: 50px; top: 30px;
    width: 360px; height: 533px;
    background: linear-gradient(180deg, #2f5d58 0%, #1b3f3b 55%, #0d2624 100%);
    border-radius: 120px 120px 0 0;
    opacity: .92;
  }

  .title {
    position: absolute;
    left: 412px; top: 150px;
    width: 380px;
    font-family: "Playfair Display", serif;
    font-weight: 400;
    font-size: 88px;
    line-height: 96px;
    color: var(--title);
    text-shadow: 0 2px 6px rgba(0,0,0,.35);
  }

  .dusk {
    position: absolute;
    left: 150px; top: 720px;
    width: 660px; height: 327px;
    background:
      radial-gradient(ellipse 120px 90px at 470px 300px, rgba(233,249,246,.95), transparent 75%),
      radial-gradient(ellipse 420px 240px at 420px 260px, var(--teal-pale), rgba(103,215,201,.45) 55%, rgba(255,255,255,0) 80%);
  }

  .copy {
    position: absolute;
    left: 43px; top: 612px;
    width: 724px;
    font-family: "Poppins", sans-serif;
    font-weight: 300;
    font-size: 14.6px;
    line-height: 19px;
    color: var(--ink);
  }
  .copy .intro { text-align: justify; }
  .drop-cap { font-weight: 500; font-size: 22px; line-height: 0; color: var(--teal-deep); }

  .details { margin-top: 19px; display: grid; grid-template-columns: 130px 1fr; row-gap: 2px; }
  .details dt { font-weight: 500; color: var(--teal-deep); }
  .details dd { color: var(--ink); }
</style>
</head>
<body>
  <main class="flyer">
    <div class="hero" role="img" aria-label="Photo of a bronze reformer statue holding a book, in front of a sunlit chapel interior with arched windows and pews">
      <div class="hero-figure"></div>
    </div>
    <h1 class="title">law and gospel</h1>

    <div class="dusk" role="img" aria-label="Soft photo of a cross silhouetted against a hazy sunset over a meadow"></div>

    <section class="copy">
      <p class="intro"><span class="drop-cap">T</span>he distinction between the law and the gospel is the most important distinction in the Christian faith. Conrad Velmer: “Distinguishing between the law and the gospel is the highest art in Christendom, one who every person who values the name Christian ought to recognize, know, and possess.” The distinction between the law and the gospel is of great comfort for the child of God. “For the law was given by Moses, but grace and truth came by Jesus Christ” (John 1:17). For these reasons, the distinction between the law and the gospel is the most heavily assaulted doctrine in the Christian faith. This Reformation Day, join us for an explanation and defense of the great distinction between God’s good law and God’s glorious gospel.</p>

      <dl class="details">
        <dt>Topic</dt><dd>The Steady Word and the Bright Promise</dd>
        <dt>Date &amp; Time</dt><dd>Tuesday, October 31, 2023 at 7:30pm</dd>
        <dt>Host</dt><dd>Harrow Creek Fellowship Church</dd>
        <dt>Speaker</dt><dd>Rev. Gerald Voskuil</dd>
        <dt>Venue</dt><dd>The Marlow Hall, 5172 Brenton Avenue, Hudsonville, MI 49318</dd>
        <dt>Format</dt><dd>Lecture followed by Q&amp;A and refreshments</dd>
      </dl>
    </section>
  </main>
</body>
</html>
```